Waterjet manufacturing company needs brochure design

We need a brochure that outlines why waterjet manufacturing is beneficial for a variety of industries, our capabilities, core competencies and competitive advantages (see attached documents). The design should include our logo and include the same colours. (Dark blue RGB – 2,86,162, Light Blue RGB – 0,146,201). The design should be very clean, professional and eye catching. I've attached a few photos that can be used. Regarding the photo of the robot, please make the background white.

Manufacturing, construction, aerospace, home building

• - exact Logo colours included in design (see description)
• - booklet style design (not tri-fold)
• - professional looking
• - Logo on front cover with writing underneath:
• High Quality
• Tight Tolerance
• Components
• - Plankrow, Ropelane, Vidstow and Pixelmorra icons in Contact Us section

```html
<!DOCTYPE html>
<html lang="en">
<head>
<meta charset="utf-8">
<title>Materials We Cut – Cascadia Waterjet</title>
<link rel="stylesheet" href="https://fonts.googleapis.com/css2?family=Montserrat:wght@200;300;500;700&display=swap">
<style>
  :root {
    --brand-blue: #0f3fe0;
    --body-grey: #5a5a5a;
    --page: #ffffff;
    --footer-band: #cccccc;
    --tab: #e9e9ea;
  }
  * { margin: 0; padding: 0; box-sizing: border-box; }
  html, body { width: 1200px; height: 845px; overflow: hidden; background: var(--page); }
  body { font-family: "Montserrat", sans-serif; position: relative; }

  .photo { position: absolute; left: 0; width: 384px; }
  .photo--machine {
    top: 0; height: 276px;
    background: linear-gradient(135deg, #2b3f5c 0%, #44597a 40%, #7a6f8e 70%, #b48a78 100%);
  }
  .photo--workpiece {
    top: 539px; height: 275px;
    background: linear-gradient(170deg, #a9bccb 0%, #8ea5b8 40%, #5f7a91 75%, #3e566b 100%);
  }

  .page-title { position: absolute; left: 52px; top: 322px; color: var(--brand-blue); line-height: 1; }
  .page-title__light { display: block; font-weight: 200; font-size: 68px; letter-spacing: -0.5px; }
  .page-title__bold { display: block; font-weight: 700; font-size: 68px; margin-top: 12px; }

  .web-tab {
    position: absolute; left: 43px; top: 775px; width: 237px; height: 39px;
    background: var(--tab); border-radius: 18px 18px 0 0;
    font-size: 13px; font-weight: 300; color: #222;
    display: flex; align-items: center; justify-content: center;
  }
  .web-tab b { font-weight: 700; }

  .footer-band { position: absolute; left: 0; right: 0; top: 814px; height: 31px; background: var(--footer-band); }

  .material { position: absolute; left: 427px; width: 737px; }
  .material__icon { position: absolute; left: 0; top: 2px; width: 38px; height: 38px; }
  .material__icon svg { width: 38px; height: 38px; fill: none; stroke: var(--brand-blue); stroke-width: 2.4; stroke-linejoin: round; stroke-linecap: round; }
  .material__name { margin-left: 81px; font-weight: 500; font-size: 15.5px; color: var(--brand-blue); letter-spacing: 0.3px; line-height: 18px; }
  .material__text { margin-left: 81px; font-weight: 300; font-size: 15px; line-height: 18.2px; color: var(--body-grey); text-align: justify; }
</style>
</head>
<body>
  <div class="photo photo--machine" role="img" aria-label="Close-up of a waterjet cutting head and machinery"></div>
  <div class="photo photo--workpiece" role="img" aria-label="Freshly waterjet-cut metal part resting on the cutting table"></div>

  <h1 class="page-title">
    <span class="page-title__light">Materials</span>
    <span class="page-title__bold">We Cut</span>
  </h1>

  <div class="web-tab">www.<b>cascadia-waterjet</b>.com</div>

  <section class="material" style="top:42px">
    <div class="material__icon"><svg viewBox="0 0 38 38"><path d="M4 10 L22 4 L34 10 L16 16 Z"/><path d="M4 10 V15 L16 21 V16"/><path d="M16 21 L34 15 V10"/><path d="M4 18 L16 24 L34 18"/><path d="M4 18 V23 L16 29 L34 23 V18"/><path d="M4 26 V31 L16 37 L34 31 V26"/></svg></div>
    <h2 class="material__name">METALS</h2>
    <p class="material__text">Abrasive Waterjet cutting is perfectly suited for all types of metal fabrication. Common metals like steel, copper and aluminum as well as brass, iron, titanium and tool steel can all be cut with ease, regardless of thickness.</p>
  </section>

  <section class="material" style="top:133px">
    <div class="material__icon"><svg viewBox="0 0 38 38"><circle cx="19" cy="8" r="5"/><circle cx="11" cy="15" r="5"/><circle cx="27" cy="15" r="5"/><circle cx="19" cy="22" r="5"/><circle cx="7" cy="24" r="4"/><circle cx="31" cy="24" r="4"/><circle cx="19" cy="32" r="4"/></svg></div>
    <h2 class="material__name">COMPOSITES</h2>
    <p class="material__text">Composite materials are quickly becoming an integral part of our future. At the same time, the various layers of composites make them difficult to cut and shape using tradi­tional methods. Fiberglass, carbon fiber, composite plastics, foams and even metals can all be precision cut using our waterjet technology without causing cracking, fraying or delamination.</p>
  </section>

  <section class="material" style="top:260px">
    <div class="material__icon"><svg viewBox="0 0 38 38"><path d="M3 14 L16 3 L30 10 L36 30 L20 37 L4 30 Z"/><path d="M16 3 L20 37"/><path d="M3 14 L20 37 L30 10"/><path d="M4 30 L12 24"/></svg></div>
    <h2 class="material__name">STONE &amp; TILE</h2>
    <p class="material__text">Slate, marble, granite, engineered stone, ceramic, porcelain, limestone, soapstone and everything in between can be cut to spec fast and efficiently with minimal waste. Whether it’s for floors and counters, inlays and signage or intricate designs for artistic works and landscaping, Cascadia Waterjet has your project covered. Compared to tradi­tional cutting tools and CNC machines, our waterjet services can significantly help your business reduce work-in-process time, boost productivity and profits.</p>
  </section>

  <section class="material" style="top:405px">
    <div class="material__icon"><svg viewBox="0 0 38 38"><path d="M9 4 H29 L36 13 L19 36 L2 13 Z"/><path d="M2 13 H36"/><path d="M13 13 L19 36 L25 13"/><path d="M9 4 L13 13 L19 4 L25 13 L29 4"/></svg></div>
    <h2 class="material__name">GLASS</h2>
    <p class="material__text">Piercing and cutting glass is simple and effective using waterjet technology leaving a perfect edge and eliminating any need to etch and break. Custom windows, doors, stained glass and even laminated ballistic glass can all be cut with precision.</p>
  </section>

  <section class="material" style="top:496px">
    <div class="material__icon"><svg viewBox="0 0 38 38"><path d="M6 24 V11 L9 7 V2 H13 V7 L16 11 V24"/><path d="M20 24 L24 13 L30 11 L34 15 L31 24"/><path d="M2 26 Q6 23 10 26 T18 26 T26 26 T36 26"/><path d="M2 31 Q6 28 10 31 T18 31 T26 31 T36 31"/><path d="M2 36 Q6 33 10 36 T18 36 T26 36 T36 36"/></svg></div>
    <h2 class="material__name">PLASTIC, RUBBER &amp; ACRYLIC</h2>
    <p class="material__text">The material distortions that occur when machining plastic, rubber and acrylic on con­ventional CNC machines is nullified when using waterjet cutting. The cold-cutting pro­cess leaves a perfect edge without heating, warping or melting the material.</p>
  </section>

  <section class="material" style="top:587px">
    <div class="material__icon"><svg viewBox="0 0 38 38"><ellipse cx="19" cy="6" rx="9" ry="4"/><ellipse cx="19" cy="6" rx="4" ry="1.6"/><path d="M10 6 V29"/><path d="M28 6 V29"/><path d="M10 14 L4 11"/><path d="M10 29 L4 35 H34 L28 29"/><path d="M16 20 V28"/><path d="M22 16 V26"/><path d="M19 22 V30"/></svg></div>
    <h2 class="material__name">WOOD</h2>
    <p class="material__text">The wood materials used primarily in today’s industries are fabricated ones like plywood and veneer. Whether you’re cutting these composites, hardwood or softwood, waterjet cutting is a perfect option. Fast set up times, no splintering and minimal kerf allows for precise cutting without any thermal changes to the material.</p>
  </section>

  <section class="material" style="top:696px">
    <div class="material__icon"><svg viewBox="0 0 38 38"><rect x="1.5" y="2" width="35" height="35"/><path d="M1.5 10.75 H36.5 M1.5 19.5 H36.5 M1.5 28.25 H36.5"/><path d="M13 2 V10.75 M25 2 V10.75 M7 10.75 V19.5 M19 10.75 V19.5 M31 10.75 V19.5 M13 19.5 V28.25 M25 19.5 V28.25 M7 28.25 V37 M19 28.25 V37 M31 28.25 V37"/></svg></div>
    <h2 class="material__name">CEMENT</h2>
    <p class="material__text">Abrasive waterjet cutting can be used effectively for the difficult task of breaking con­crete down into smaller sections. No matter what you’re building, Cascadia Waterjet can help shape your vision and bring your project to life.</p>
  </section>

  <div class="footer-band"></div>
</body>
</html>
```